Print on top the name of the company: (Or Similar)
Larkmoor Cleaning & Disinfecting
Because your standards aren't standard.

We adhere to ALL NVB guidelines for both residential and commercial cleaning.

Infection Control is our ultimate goal.

Instructions:
Opening a residential and commercial cleaning and disinfecting company in south Florida.

Targeting high-end residential clients, commercial and healthcare facilities, specializing in Ambulatory Care Guidelines. With a concentration and expertise in targeting Covid 19 and other transmissible pathogens.

UMRE trained.
Owned and operated by a licensed BSN Registered Nurse specially ​trained in Infection Control Prevention with over 25 years experience. Over two decades in Ambulatory Surgery Center Administration, Director of Nursing and Infection Control Prevention ad Consulting.

Looking to create a business flier that emphasizes Cleaning & Disinfection
along with the standard expectation for residential and Commercial cleaning services
Updates

Need extra days to review

Target Market(s)

Residential & Commercial

Font styles to use
Decorative

Requirements
Must have
• A checklist for cleaning services

```html
<!DOCTYPE html>
<html lang="en">
<head>
<meta charset="utf-8">
<title>Larkmoor Cleaning &amp; Disinfecting</title>
<link href="https://fonts.googleapis.com/css2?family=Montserrat:wght@400;500;600;700;800;900&display=swap" rel="stylesheet">
<style>
  :root {
    --navy: #0d2a63;
    --navy-deep: #081d48;
    --blue: #1d55b5;
    --blue-mid: #2a6ad0;
    --sky: #dbe8f6;
    --white: #ffffff;
    --ink: #1c2a45;
    --card: #f3f6fb;
  }
  * { box-sizing: border-box; margin: 0; padding: 0; }
  html, body { width: 738px; height: 1200px; overflow: hidden; background: #e6e6e6; }
  body { font-family: "Montserrat", sans-serif; color: var(--ink); }
  .flyer { position: relative; width: 738px; height: 1200px; background: var(--white); overflow: hidden; }

  .hero { position: absolute; left: 0; top: 0; width: 738px; height: 350px; }
  .hero-photo {
    position: absolute; right: 0; top: 0; width: 370px; height: 350px;
    background: linear-gradient(135deg, #f4f8fc 0%, #c9dcef 45%, #7fa6d3 100%);
  }
  .hero-text { position: absolute; left: 36px; top: 34px; width: 360px; }
  .company {
    font-weight: 900; font-size: 36px; line-height: 1.05; color: var(--navy);
    text-transform: uppercase; letter-spacing: -0.3px;
  }
  .goal {
    margin-top: 14px; font-weight: 800; font-size: 27px; line-height: 1.08;
    color: var(--blue); text-transform: uppercase;
  }
  .adhere { margin-top: 18px; font-weight: 700; font-size: 15px; line-height: 1.35; color: var(--navy); }

  .info {
    position: absolute; left: 0; top: 350px; width: 738px; height: 400px;
    background: linear-gradient(160deg, var(--blue-mid) 0%, var(--blue) 40%, var(--navy) 100%);
    color: var(--white); padding: 26px 36px;
  }
  .info-label {
    display: inline-block; background: var(--white); color: var(--navy);
    font-weight: 800; font-size: 17px; padding: 6px 16px; text-transform: uppercase;
  }
  .info p { margin-top: 12px; font-size: 12.5px; line-height: 1.55; font-weight: 500; }
  .info h3 { margin-top: 20px; font-size: 19px; font-weight: 800; text-transform: uppercase; }

  .services {
    position: absolute; left: 36px; top: 640px; width: 666px; height: 440px;
    display: flex; gap: 26px;
  }
  .service {
    flex: 1; background: var(--card); border-top: 6px solid var(--blue);
    text-align: center; padding: 24px 18px;
    box-shadow: 0 6px 18px rgba(8, 29, 72, 0.25);
  }
  .service-icon { width: 58px; height: 58px; margin: 0 auto; }
  .service h4 {
    margin: 12px 0 14px; font-size: 22px; font-weight: 900; color: var(--blue);
    text-transform: uppercase; letter-spacing: 0.5px;
  }
  .service ul { list-style: none; }
  .service li { font-size: 14.5px; font-weight: 600; line-height: 1.95; color: var(--ink); }

  .call {
    position: absolute; left: 0; bottom: 0; width: 738px; height: 92px;
    background: var(--navy-deep); color: var(--white);
    display: flex; align-items: center; justify-content: center;
    font-weight: 800; font-size: 28px; letter-spacing: 0.5px; text-transform: uppercase;
    border-top: 8px solid var(--blue);
  }
</style>
</head>
<body>
<main class="flyer">
  <section class="hero">
    <div class="hero-photo" role="img" aria-label="Cleaning technician in protective suit spraying disinfectant in a bright office"></div>
    <div class="hero-text">
      <h1 class="company">Larkmoor Cleaning &amp; Disinfecting</h1>
      <h2 class="goal">Infection control is our ultimate goal</h2>
      <p class="adhere">We adhere to ALL NVB guidelines for both residential and commercial cleaning.</p>
    </div>
  </section>

  <section class="info">
    <span class="info-label">Instructions:</span>
    <p>Opening a residential and commercial cleaning and disinfecting company in south Florida. Targeting high-end residential clients, commercial and healthcare facilities, specializing in Ambulatory Care Guidelines. With a concentration and expertise in targeting Covid 19 and other transmissible pathogens.</p>
    <h3>UMRE Trained</h3>
    <p>Owned and operated by a licensed BSN Registered Nurse specially trained in Infection Control Prevention with over 25 years experience. Over two decades in Ambulatory Surgery Center Administration, Director of Nursing and Infection Control Prevention and Consulting.</p>
  </section>

  <section class="services">
    <article class="service">
      <svg class="service-icon" viewBox="0 0 58 58" aria-hidden="true">
        <circle cx="29" cy="29" r="29" fill="#1d55b5"/>
        <rect x="19" y="16" width="20" height="27" fill="none" stroke="#fff" stroke-width="2.5"/>
        <g fill="#fff"><rect x="23" y="20" width="4" height="4"/><rect x="31" y="20" width="4" height="4"/><rect x="23" y="28" width="4" height="4"/><rect x="31" y="28" width="4" height="4"/><rect x="26" y="36" width="6" height="7"/></g>
      </svg>
      <h4>Commercial</h4>
      <ul>
        <li>Janitorial</li><li>Offices</li><li>Floor Maintenance</li><li>Carpet Cleaning</li>
        <li>Move - Ins</li><li>Move - Outs</li><li>Constructions Clean - Ups</li><li>Estate Clean - Outs</li>
      </ul>
    </article>
    <article class="service">
      <svg class="service-icon" viewBox="0 0 58 58" aria-hidden="true">
        <circle cx="29" cy="29" r="29" fill="#1d55b5"/>
        <path d="M15 29 L29 17 L43 29" fill="none" stroke="#fff" stroke-width="2.8" stroke-linejoin="round"/>
        <path d="M19 27 V42 H39 V27" fill="none" stroke="#fff" stroke-width="2.5"/>
        <rect x="26" y="33" width="6" height="9" fill="#fff"/>
      </svg>
      <h4>Residential</h4>
      <ul>
        <li>House Cleaning</li><li>Before And After Party</li><li>Move - Ins</li><li>Move - Outs</li>
        <li>Holiday Cleaning</li><li>Seasonal Cleaning</li><li>Carpet Cleaning</li><li>Deodorizing And Sanitizing</li>
      </ul>
    </article>
  </section>

  <footer class="call">Please call us at: (415) 555 01 87</footer>
</main>
</body>
</html>
```